Need a business card design for a new business

The business is going to be called "The Maple Lectern" - it is an online training company that provides Instructor Lead training to students at any destination in the world
The reference to cloud is the internet and classroom reference will be a computer at the students and instructors end

We will need a Web site and stationary and advertising material developed over time but for now require the business cards only

So if we are happy with the business card then we will use the same designers for the other requirments of the business as it evolves

Industry/Entity Type

Advertising

```html
<!DOCTYPE html>
<html lang="en">
<head>
<meta charset="utf-8">
<title>The Maple Lectern – Business Card</title>
<link rel="stylesheet" href="https://fonts.googleapis.com/css2?family=Mali:wght@500&family=Delius&family=Kreon:wght@400&display=swap">
<style>
  :root {
    --backdrop: #16161b;
    --card: #000000;
    --card-edge: #e9e9e9;
    --ink: #ffffff;
    --ink-soft: #e4e4e4;
    --accent: #4b2a8c;
  }
  * { box-sizing: border-box; margin: 0; padding: 0; }
  html, body {
    width: 752px;
    height: 1200px;
    overflow: hidden;
    background: var(--backdrop);
  }
  .canvas {
    position: relative;
    width: 752px;
    height: 1200px;
  }
  .card {
    position: absolute;
    background: var(--card);
    border: 2px solid var(--card-edge);
  }
  .card--front {
    left: 73px; top: 123px;
    width: 629px; height: 367px;
  }
  .card--back {
    left: 53px; top: 680px;
    width: 677px; height: 366px;
  }
  .brand {
    position: absolute;
    display: flex;
    align-items: center;
    gap: 14px;
    font-family: "Mali", "Comic Sans MS", cursive;
    font-weight: 500;
    color: var(--ink);
    white-space: nowrap;
  }
  .brand__dot {
    display: inline-block;
    border-radius: 50%;
    background: var(--accent);
  }
  .card--front .brand {
    left: 0; right: 0; top: 150px;
    justify-content: center;
    font-size: 52px;
  }
  .card--front .brand__dot { width: 30px; height: 30px; }
  .card--back .brand {
    left: 26px; top: 118px;
    font-size: 29px;
    gap: 10px;
  }
  .card--back .brand__dot { width: 18px; height: 18px; }
  .holder {
    position: absolute;
    right: 36px; top: 28px;
    text-align: right;
  }
  .holder__name {
    font-family: "Delius", "Comic Sans MS", cursive;
    font-size: 35px;
    letter-spacing: 1.5px;
    color: var(--ink);
    line-height: 1.1;
  }
  .holder__role {
    font-family: "Delius", "Comic Sans MS", cursive;
    font-size: 21px;
    color: var(--ink);
    margin-right: 4px;
  }
  .contact {
    position: absolute;
    left: 285px; top: 172px;
    list-style: none;
    font-family: "Kreon", Georgia, serif;
    font-size: 23px;
    line-height: 31.5px;
    color: var(--ink-soft);
  }
</style>
</head>
<body>
<main class="canvas">
  <section class="card card--front" aria-label="Card front">
    <div class="brand"><span class="brand__dot"></span>The Maple Lectern</div>
  </section>

  <section class="card card--back" aria-label="Card back">
    <div class="brand"><span class="brand__dot"></span>The Maple Lectern</div>
    <div class="holder">
      <p class="holder__name">Dana Verlo</p>
      <p class="holder__role">Manager</p>
    </div>
    <ul class="contact">
      <li>Phone: 555-014-2387</li>
      <li>Fax: 555-014-9062</li>
      <li>Email:info@mlmail.com</li>
      <li>1427 Birchwood Ln.</li>
      <li>Ashford, IA 50010</li>
      <li>www.TheMapleLectern.com</li>
    </ul>
  </section>
</main>
</body>
</html>
```